K&M Trailer Rental promo Flyer 5.5x8.5" Flyer

All assets and several pictures of my trailers, that we rent out, are attached.

Flyer dimensions are 5.5"x8.5" - I'll be having it printed on glossy stock.
The dimensions and capacity of the trailers is key.
Include phone number: 248-555-0186 and our website kandmtrailer-example.com

I want something that will really "POP".

Target Market(s)

Blue collar business owners. Recreational offer roads/4x4 folks, used car dealers, contractors/small business owners. Folks with only occasional need for a trailer

Industry/Entity Type

Trailer Rental

Font styles to use
Other font styles liked:
• Designer's choice/no preference

Colors
EE7325
F08F49
F5BC92
FAE3D3
FDF4ED

Requirements
Must have
• Phone number, website, and details about our trailer offerings

```html
<!DOCTYPE html>
<html lang="en">
<head>
<meta charset="utf-8">
<title>K&amp;M Trailer Rental Flyer</title>
<link rel="stylesheet" href="https://fonts.googleapis.com/css2?family=Bebas+Neue&family=Montserrat:wght@400;500;600;700&display=swap">
<style>
  :root {
    --accent: #ee7325;
    --accent-soft: #f08f49;
    --accent-pale: #fae3d3;
    --ink: #111416;
    --paper: #ffffff;
    --backdrop: #d0d0d0;
    --body: #1d1d1f;
  }
  * { margin: 0; padding: 0; box-sizing: border-box; }
  html, body { width: 954px; height: 1200px; overflow: hidden; background: var(--backdrop); }
  .canvas { position: relative; width: 954px; height: 1200px; background: var(--backdrop); }
  .flyer { position: absolute; left: 112px; top: 84px; width: 730px; height: 1030px; background: var(--paper); overflow: hidden; }
  .photo-art { position: absolute; left: 0; top: 0; width: 730px; height: 1030px; }
  .wordmark {
    position: absolute; left: 39px; top: 134px;
    font-family: "Bebas Neue", sans-serif; font-size: 44px; line-height: 1;
    color: var(--ink); white-space: nowrap;
  }
  .headline { position: absolute; left: 40px; top: 214px; font-family: "Bebas Neue", sans-serif; font-weight: 400; line-height: 1; font-size: 106px; }
  .headline span { display: block; height: 92px; }
  .headline .accent { color: var(--accent); }
  .headline .dark { color: var(--ink); }
  .tagline { position: absolute; left: 41px; top: 502px; font-family: "Bebas Neue", sans-serif; font-size: 47px; line-height: 1; color: var(--ink); white-space: nowrap; }
  .fleet-frame { position: absolute; left: 29px; top: 578px; width: 190px; height: 240px; border-top: 2px solid var(--accent); border-left: 2px solid var(--accent); border-top-left-radius: 18px; }
  .fleet-title { position: absolute; left: 41px; top: 585px; font-family: "Montserrat", sans-serif; font-weight: 700; font-size: 28px; line-height: 1.1; color: var(--accent); }
  .fleet-lead { position: absolute; left: 41px; top: 618px; font-family: "Montserrat", sans-serif; font-weight: 600; font-size: 18px; line-height: 22px; color: var(--ink); }
  .about { position: absolute; left: 41px; top: 681px; width: 367px; font-family: "Montserrat", sans-serif; font-size: 11.9px; line-height: 14.8px; color: var(--body); text-align: justify; }
  .about strong { font-weight: 700; }
  .specs { position: absolute; left: 41px; top: 812px; width: 367px; list-style: none; font-family: "Montserrat", sans-serif; font-size: 11.5px; line-height: 16px; color: var(--body); }
  .specs strong { color: var(--accent); font-weight: 700; }
  .cta { position: absolute; left: 41px; top: 860px; font-family: "Montserrat", sans-serif; font-weight: 700; font-size: 25.5px; line-height: 1.1; color: var(--ink); }
  .phone { position: absolute; left: 38px; top: 886px; font-family: "Montserrat", sans-serif; font-weight: 600; font-size: 41px; line-height: 1.1; color: var(--accent); }
  .contact { position: absolute; left: 36px; top: 946px; font-family: "Montserrat", sans-serif; font-size: 18.5px; line-height: 23px; color: var(--ink); }
</style>
</head>
<body>
<div class="canvas">
  <div class="flyer">
    <svg class="photo-art" viewBox="0 0 730 1030" xmlns="http://www.w3.org/2000/svg">
      <defs>
        <linearGradient id="yardPhoto" x1="0" y1="0" x2="0" y2="1">
          <stop offset="0" stop-color="#8fb8e4"/>
          <stop offset="0.3" stop-color="#5e7a4c"/>
          <stop offset="0.55" stop-color="#6f8a55"/>
          <stop offset="0.65" stop-color="#3b3a36"/>
          <stop offset="0.72" stop-color="#b9a58c"/>
          <stop offset="1" stop-color="#a89277"/>
        </linearGradient>
        <linearGradient id="lotPhoto" x1="0" y1="0" x2="0" y2="1">
          <stop offset="0" stop-color="#9fbde0"/>
          <stop offset="0.2" stop-color="#4d5655"/>
          <stop offset="0.5" stop-color="#3b3f44"/>
          <stop offset="1" stop-color="#2c2f33"/>
        </linearGradient>
        <linearGradient id="deckPhoto" x1="0" y1="0" x2="0" y2="1">
          <stop offset="0" stop-color="#b3b2ad"/>
          <stop offset="0.5" stop-color="#a6a49f"/>
          <stop offset="1" stop-color="#8f8d89"/>
        </linearGradient>
      </defs>
      <circle cx="603" cy="232" r="278" fill="none" stroke="var(--accent)" stroke-width="7"/>
      <g role="img" aria-label="Photo of a compact car strapped onto a black flatbed car trailer in a residential yard">
        <circle cx="603" cy="232" r="271" fill="url(#yardPhoto)"/>
      </g>
      <circle cx="612" cy="626" r="164" fill="none" stroke="var(--accent)" stroke-width="6"/>
      <g role="img" aria-label="Photo of an equipment trailer tongue and jack in a paved parking lot">
        <circle cx="612" cy="626" r="159" fill="url(#lotPhoto)"/>
      </g>
      <circle cx="612" cy="941" r="172" fill="none" stroke="var(--accent)" stroke-width="6"/>
      <g role="img" aria-label="Photo of a new wood-deck flatbed trailer parked on asphalt">
        <circle cx="612" cy="941" r="167" fill="url(#deckPhoto)"/>
      </g>
    </svg>

    <div class="wordmark">K&amp;M Trailer Rental</div>

    <h1 class="headline">
      <span class="accent">K&amp;M</span>
      <span class="dark">TRAILER</span>
      <span class="accent">RENTAL</span>
    </h1>

    <div class="tagline">CAR / EQUIPMENT TRAILERS</div>

    <div class="fleet-frame"></div>
    <h2 class="fleet-title">OUR FLEET</h2>
    <p class="fleet-lead">These are the trailers<br>we have available to offer you.</p>
    <p class="about"><strong>K&amp;M Trailer Rental,</strong> based in Maple Ridge, MI, is a trusted and reliable provider of high-quality trailer rentals. Serving the local community and surrounding areas, we specialize in offering a diverse selection of trailers designed to meet a variety of hauling and transportation needs. Whether you're looking for a trailer to move equipment, transport a vehicle, or complete a large-scale construction project, K&amp;M Trailer Rental is your one-stop solution.</p>
    <ul class="specs">
      <li><strong>Car Hauler:</strong> 18' x 83" deck &middot; 7,000 lb capacity</li>
      <li><strong>Equipment:</strong> 20' x 83" deck &middot; 10,000 lb capacity</li>
    </ul>

    <div class="cta">CALL US NOW!</div>
    <div class="phone">(248)555-0186</div>
    <div class="contact">Maple Ridge, MI<br>www.kandmtrailer-example.com</div>
  </div>
</div>
</body>
</html>
```